Seafood Restaurant Outdoor Menu Board

Corlen's Seafood, a legendary local seafood restaurant in Ventura, CA USA, most widely known for its fish and chips and clam chowder, needs refreshed outdoor menu boards!

You can see the existing menu board at https://www.photoshare-example.net/p/X9kB2Lmq41T/

and get inspiration from our website, https://corlensseafood-example.net

Please use your design for 2 sets of menu items, to be displayed side by side as in the photo:
Menu Board #1: "Customer Favorites"
- Grilled Halibut
- Grilled Salmon Filet
- Grilled Shrimp Skewers
- Corlen's Fish & Chips
- 14pc Shrimp & Chips
- Harbor Trio
- Onion Rings
- Clam Chowder Skiff
- Large Clam Chowder
- Small Clam Chowder
Menu Board #2: "Grilled Dinners"
GR HALIBUT $21.80
BAKED HALIBUT $26.95
GR SNAPPER $21.95
GR AHI $25.85
GR SALMON FILLET $20.90
GR YELLOWTAIL $12.65
GR BLACK SEA BASS $20.99
GR SHRIMP SKEWERS $23.10
GR WHITE SEA BASS $21.60
GR SWORDFISH $27.75
GR MAHI $7.95
GR COD $10.40

SERVED WITH RICE PILAF & BREAD & YOUR CHOICE OF PASTA SALAD, COLE SLAW, OR GREEN SALAD

Our landlord has provided the following guidelines for the new menu board:
- Public Facing Exterior Menu boards need overall simplification and reduction of the information offered while still highlighting major sellers and up sellers.
- Need to be designed as elegant wall signs rather than a list of menu items. (see examples)
- Less is More.
- Easy to read and understand, equally spaced information, good use of negative space.
- Draw customers eyes to the most desirable products.
- Layout: The layout should be professionally done, with sufficient negative space around menu items.
- Fonts: 3 Fonts maximum, encouraging sans serif font styles for easy readability.
- Established 1982: Arial Rounded MT Bold
- Menu Boards: Myriad Pro - Bold Condensed
- Smaller Directional Signs: Arial
- Colors: Tied to organization branding, 3 colors maximum. Please use a light-colored background. Our brand colors are:
- Primary: #233F94
- Secondary: #0F65A7
- Tertiary: 32A0CA
- Contrast: #F7F4DB
Attention: #ED4224
Icons: Use of simplified icons are allowed and encouraged to highlight and organize menu sections

```html
<!DOCTYPE html>
<html lang="en">
<head>
<meta charset="utf-8">
<title>Corlen's Seafood – Menu Boards</title>
<link rel="stylesheet" href="https://fonts.googleapis.com/css2?family=Graduate&family=Poppins:wght@500;700;800&display=swap">
<style>
  :root{
    --brand-blue:#2c45a5;
    --brand-light:#2ba6dc;
    --paper:#ffffff;
    --backdrop:#ecebe6;
  }
  *{box-sizing:border-box;margin:0;padding:0}
  html,body{width:1200px;height:2252px;overflow:hidden;background:var(--backdrop)}
  .canvas{position:relative;width:1200px;height:2252px}

  .board{position:absolute;left:290px;width:620px;height:980px;background:var(--paper);overflow:hidden;box-shadow:0 6px 20px rgba(0,0,0,.12)}
  .board--favorites{top:73px}
  .board--dinners{top:1199px}

  .section{position:absolute;left:0;width:100%;overflow:hidden}
  .section--light{background:var(--paper)}
  .section--blue{background:var(--brand-blue)}

  .frame{position:absolute;pointer-events:none}
  .frame--outer{left:22px;right:22px;border-width:3px}
  .frame--inner{left:36px;right:36px;border-width:2px}
  .frame--open-bottom{border-style:solid solid none solid;top:22px;bottom:0}
  .frame--open-bottom.frame--inner{top:36px}
  .frame--open-top{border-style:none solid solid solid;top:0;bottom:22px}
  .frame--open-top.frame--inner{bottom:36px}
  .frame--blue{border-color:var(--brand-blue)}
  .frame--white{border-color:var(--paper)}

  .brand-name{position:absolute;left:0;width:100%;text-align:center;top:78px;font-family:'Poppins',sans-serif;font-weight:800;font-size:38px;letter-spacing:.5px}
  .brand-name--blue{color:var(--brand-blue)}
  .brand-name--white{color:var(--paper)}

  .headline{position:absolute;left:0;width:100%;text-align:center;font-family:'Graduate',serif;line-height:1}
  .headline--fresh{font-size:60px;top:192px;color:var(--brand-blue)}
  .headline--menu{font-size:156px;top:258px;color:var(--brand-blue);letter-spacing:-2px}
  .board--dinners .headline--fresh{font-size:52px;top:168px;color:var(--brand-light)}
  .board--dinners .headline--menu{font-size:136px;top:228px;color:var(--paper)}

  .outline-title{font-family:'Poppins',sans-serif;font-weight:500;color:transparent;-webkit-text-stroke:2px var(--paper);line-height:.98}
  .category-vertical{position:absolute;left:70px;top:24px;height:510px;writing-mode:vertical-rl;transform:rotate(180deg);font-size:64px;letter-spacing:1px;text-align:center}
  .category-title{position:absolute;left:0;width:100%;top:372px;text-align:center;font-size:72px;letter-spacing:-1px}

  .favorites-list{position:absolute;left:268px;top:36px;width:288px;list-style:none}
  .favorites-list li{font-family:'Poppins',sans-serif;font-weight:700;font-size:19px;color:var(--paper);height:48px;line-height:46px;border-bottom:1px dotted rgba(255,255,255,.8);white-space:nowrap}
  .favorites-list li:last-child{border-bottom:none}

  .price-grid{position:absolute;top:40px;list-style:none}
  .price-grid--left{left:52px;width:255px}
  .price-grid--right{left:345px;width:225px}
  .price-item{position:relative;font-family:'Poppins',sans-serif;font-weight:800;font-size:20px;line-height:1.05;color:var(--brand-blue);padding-right:82px}
  .price-tag{position:absolute;right:0;top:-2px;width:66px;height:21px;background:var(--brand-blue);color:var(--paper);font-size:13px;font-weight:700;text-align:center;line-height:21px}
</style>
</head>
<body>
<main class="canvas">

  <section class="board board--favorites" aria-label="Customer favorites menu board">
    <div class="section section--light" style="top:0;height:406px">
      <div class="frame frame--outer frame--blue frame--open-bottom"></div>
      <div class="frame frame--inner frame--blue frame--open-bottom"></div>
      <p class="brand-name brand-name--blue">Corlen's Seafood</p>
      <h1 class="headline headline--fresh">FRESH SEAFOOD</h1>
      <h2 class="headline headline--menu" style="top:262px">MENU</h2>
    </div>
    <div class="section section--blue" style="top:406px;height:574px">
      <div class="frame frame--outer frame--white frame--open-top"></div>
      <div class="frame frame--inner frame--white frame--open-top"></div>
      <h3 class="outline-title category-vertical">CUSTOMER FAVORITES</h3>
      <ul class="favorites-list">
        <li>GRILLED HALIBUT</li>
        <li>GRILLED SALMON FILET</li>
        <li>GRILLED SHRIMP SKEWERS</li>
        <li>CORLEN'S FISH &amp; CHIPS</li>
        <li>14PC SHRIMP &amp; CHIPS</li>
        <li>HARBOR TRIO</li>
        <li>ONION RINGS</li>
        <li>CLAM CHOWDER SKIFF</li>
        <li>LARGE CLAM CHOWDER</li>
        <li>SMALL CLAM CHOWDER</li>
      </ul>
    </div>
  </section>

  <section class="board board--dinners" aria-label="Grilled dinners menu board">
    <div class="section section--blue" style="top:0;height:505px">
      <div class="frame frame--outer frame--white frame--open-bottom"></div>
      <div class="frame frame--inner frame--white frame--open-bottom"></div>
      <p class="brand-name brand-name--white">Corlen's Seafood</p>
      <h1 class="headline headline--fresh">FRESH SEAFOOD</h1>
      <h2 class="headline headline--menu">MENU</h2>
      <h3 class="outline-title category-title">GRILLED<br>DINNERS</h3>
    </div>
    <div class="section section--light" style="top:505px;height:475px">
      <div class="frame frame--outer frame--blue frame--open-top"></div>
      <div class="frame frame--inner frame--blue frame--open-top"></div>
      <ul class="price-grid price-grid--left">
        <li class="price-item" style="margin-top:12px">GR HALIBUT<span class="price-tag">$21.80</span></li>
        <li class="price-item" style="margin-top:22px">BAKED<br>HALIBUT<span class="price-tag">$26.95</span></li>
        <li class="price-item" style="margin-top:14px">GR SNAPPER<span class="price-tag">$21.95</span></li>
        <li class="price-item" style="margin-top:26px">GR AHI<span class="price-tag">$25.85</span></li>
        <li class="price-item" style="margin-top:26px">GR SALMON<br>FILLET<span class="price-tag">$20.90</span></li>
        <li class="price-item" style="margin-top:26px">GR<br>YELLOWTAIL<span class="price-tag">$12.65</span></li>
        <li class="price-item" style="margin-top:22px">GR COD<span class="price-tag">$10.40</span></li>
      </ul>
      <ul class="price-grid price-grid--right">
        <li class="price-item" style="margin-top:10px">GR BLACK<br>SEA BASS<span class="price-tag">$20.99</span></li>
        <li class="price-item" style="margin-top:34px">GR SHRIMP<br>SKEWERS<span class="price-tag">$23.10</span></li>
        <li class="price-item" style="margin-top:34px">GR WHITE<br>SEA BASS<span class="price-tag">$21.60</span></li>
        <li class="price-item" style="margin-top:36px">GR<br>SWORDFISH<span class="price-tag">$27.75</span></li>
        <li class="price-item" style="margin-top:32px">GR MAHI<span class="price-tag">$7.95</span></li>
      </ul>
    </div>
  </section>

</main>
</body>
</html>
```